Rivet Athletic Supply Inc.

Need to create a website that is informational and has the ability to sell goods and services. Such as a custom t shirt designer where the user can upload and image to be displayed on the garmet. The sports we specialize in are basketball, football, and baseball.

Would like like:
Home Page
Locker Room Page:
Custom Uniforms Page
Custom Shirt Creator
Brands
About

Competitor websites are
lornfieldsportsco.example
qtv.example
wmdgear.example

```html
<!DOCTYPE html>
<html lang="en">
<head>
<meta charset="UTF-8">
<title>Rivet Athletic Supply — Custom Sports Apparel</title>
<link href="https://fonts.googleapis.com/css2?family=Poppins:wght@400;500;600;700;800&display=swap" rel="stylesheet">
<style>
:root{
  --blue:#1f5cab;
  --blue-mid:#2666b8;
  --blue-light:#2b6dc0;
  --blue-bright:#2f86e6;
  --red:#e2383f;
  --red-deep:#b92a33;
  --navy:#16223b;
  --ink:#2b2f38;
  --muted:#5d6370;
  --white:#ffffff;
  --shadow:rgba(20,30,60,.14);
}
*{margin:0;padding:0;box-sizing:border-box}
html,body{width:1200px;height:3844px;overflow:hidden}
body{font-family:"Poppins",sans-serif;color:var(--ink);background:var(--white);position:relative}
.abs{position:absolute}
.btn{display:inline-block;font-size:10px;font-weight:600;text-transform:uppercase;letter-spacing:.4px;padding:11px 20px;border-radius:3px;color:var(--white);white-space:nowrap}
.btn-red{background:var(--red)}
.btn-blue{background:var(--blue)}
.btn-outline{border:1.5px solid var(--white)}
.red{color:var(--red)}

/* navigation */
.site-nav{left:0;top:0;width:1200px;height:80px;background:var(--white);display:flex;align-items:center;padding:0 64px;justify-content:space-between;z-index:3;box-shadow:0 1px 4px rgba(0,0,0,.06)}
.nav-links{display:flex;gap:26px;font-size:10px;font-weight:600;text-transform:uppercase;color:var(--navy);align-items:center}
.nav-links .home-dot{width:8px;height:8px;border-radius:50%;background:var(--blue)}
.nav-links .active{color:var(--blue)}
.brand{display:flex;align-items:center;gap:8px;font-weight:800;font-size:20px;color:var(--red);text-transform:uppercase;letter-spacing:.3px;white-space:nowrap}
.brand .mark{width:14px;height:14px;background:var(--red)}

/* hero */
.hero{left:0;top:80px;width:1200px;height:592px;background:linear-gradient(100deg,#c92f36 0%,#e0464b 50%,#e85a4e 100%);overflow:hidden}
.hero-photo{left:0;top:0}
.hero-copy{left:128px;top:170px;width:460px;color:var(--white)}
.hero-copy h1{font-size:40px;line-height:1.08;font-weight:800;text-transform:uppercase}
.hero-copy h1 .accent{color:var(--blue-bright)}
.hero-copy p{font-size:12px;line-height:1.55;margin:20px 0 30px;max-width:330px}
.hero-copy .actions{display:flex;gap:12px}
.hero-dots{left:1000px;top:552px;display:flex;gap:8px}
.hero-dots span{width:7px;height:7px;border-radius:50%;background:rgba(255,255,255,.5)}
.hero-dots span.on{background:var(--white)}

/* section titles */
.section-title{font-weight:800;text-transform:uppercase;color:var(--blue);text-align:center;width:1200px;left:0;white-space:nowrap}

/* gear cards */
.gear{left:128px;top:832px;width:944px;display:flex;gap:10px}
.gear-card{width:228px;height:328px}
.gear-card .pic{height:200px;width:100%}
.gear-card .info{height:128px;background:var(--blue);color:var(--white);padding:26px 18px}
.gear-card h3{font-size:13px;font-weight:700;text-transform:uppercase;margin-bottom:8px;white-space:nowrap}
.gear-card p{font-size:10px;line-height:1.5;opacity:.9}

/* locker room */
.locker-photo{left:192px;top:1260px;width:344px;height:420px;background:linear-gradient(180deg,#56616c 0%,#c89a3c 40%,#b98f3e 62%,#6f7b7d 100%)}
.locker-copy{left:584px;top:1336px;width:420px}
.split-title{font-size:24px;font-weight:800;text-transform:uppercase;color:var(--navy);line-height:1.15;white-space:nowrap}
.locker-copy p,.shirt-copy p{font-size:10.5px;line-height:1.6;color:var(--muted);margin-top:14px}

/* uniforms band */
.uniforms{left:0;top:1760px;width:1200px;height:420px;background:var(--blue);overflow:hidden}
.uniforms svg{position:absolute;left:0;top:0}
.uniforms-copy{left:128px;top:150px;width:540px;color:var(--white)}
.uniforms-copy h2{font-size:26px;font-weight:800;text-transform:uppercase;white-space:nowrap}
.uniforms-copy p{font-size:10.5px;line-height:1.6;margin:10px 0 20px;opacity:.92;max-width:460px}
.jersey{left:740px;top:56px;width:330px;height:308px;border-radius:18px;background:linear-gradient(160deg,#2a2f37 0%,#1b1f26 60%,#3a3522 100%);box-shadow:0 10px 30px rgba(0,0,0,.25)}

/* shirt creator */
.shirt-photo{left:128px;top:2300px;width:480px;height:460px;background:linear-gradient(160deg,#1f2835 0%,#3f4958 55%,#aab2bd 100%)}
.shirt-copy{left:648px;top:2424px;width:420px}
.shirt-copy .btn{margin-top:20px}

/* brands */
.brands-sub{left:0;width:1200px;top:2912px;text-align:center;font-size:11px;color:var(--muted)}
.brand-row{left:216px;top:2944px;width:768px;display:flex;justify-content:space-between}
.brand-chip{width:128px;height:128px;border-radius:50%;background:var(--white);box-shadow:0 2px 10px var(--shadow);display:flex;align-items:center;justify-content:center;gap:6px;font-size:15px;font-weight:700;color:var(--navy)}
.brand-chip .dot{width:10px;height:10px;border-radius:50%;background:var(--navy)}

/* about */
.about{left:0;top:3188px;width:1200px;height:292px;background:linear-gradient(180deg,#e14b4a 0%,#dd3d42 100%);color:var(--white);text-align:center;overflow:hidden}
.about h2{font-size:28px;font-weight:800;text-transform:uppercase;margin-top:84px}
.about p{font-size:10.5px;line-height:1.6;width:560px;margin:12px auto 20px;opacity:.95}

/* footer */
.site-footer{left:0;top:3480px;width:1200px;height:364px;background:var(--blue);color:var(--white)}
.footer-brand{left:0;top:82px;width:1200px;justify-content:center;color:var(--white);font-size:28px}
.footer-brand .mark{background:var(--white);width:20px;height:20px}
.footer-links{left:0;top:172px;width:1200px;display:flex;justify-content:center;gap:34px;font-size:10px;font-weight:600;text-transform:uppercase}
.socials{left:0;top:222px;width:1200px;display:flex;justify-content:center;gap:14px}
.socials span{width:26px;height:26px;border-radius:50%;background:var(--red)}
.footer-rule{left:64px;top:280px;width:1072px;height:1px;background:rgba(255,255,255,.35)}
.copyright{left:0;top:318px;width:1200px;text-align:center;font-size:10px;opacity:.9}
.to-top{left:1134px;top:3774px;width:34px;height:34px;border-radius:50%;background:var(--red)}
</style>
</head>
<body>

<header class="site-nav abs">
  <nav class="nav-links">
    <span class="home-dot"></span>
    <span class="active">Locker Room</span>
    <span>Custom Uniforms</span>
    <span>Custom Shirt Creator</span>
  </nav>
  <div class="brand"><span class="mark"></span>Rivet Athletic Supply</div>
  <nav class="nav-links">
    <span>Brands</span>
    <span>About Us</span>
    <svg width="12" height="12" viewBox="0 0 12 12" aria-hidden="true"><circle cx="5" cy="5" r="3.8" stroke="#16223b" stroke-width="1.5" fill="none"/><path d="M8 8 L11 11" stroke="#16223b" stroke-width="1.5"/></svg>
    <span class="btn btn-red">Shop Now</span>
  </nav>
</header>

<section class="hero abs">
  <svg class="hero-photo abs" width="1200" height="592" viewBox="0 0 1200 592" role="img" aria-label="Basketball player in a red jersey leaping toward a hoop">
    <defs>
      <linearGradient id="heroShade" x1="0" y1="0" x2="1" y2="1">
        <stop offset="0" stop-color="#a8252f"/>
        <stop offset="1" stop-color="#d8454a"/>
      </linearGradient>
    </defs>
    <polygon points="640,0 1200,0 1200,592 560,592" fill="url(#heroShade)"/>
  </svg>
  <div class="hero-copy abs">
    <h1><span class="accent">Custom</span> Sports<br>Apparel Built<br>For <span class="accent">Champions</span></h1>
    <p>Premium custom uniforms, team gear, and personalized apparel for basketball, football, and baseball.</p>
    <div class="actions">
      <span class="btn btn-blue">Design Your Uniform</span>
      <span class="btn btn-outline">Create Your Shirt</span>
    </div>
  </div>
  <div class="hero-dots abs"><span class="on"></span><span></span><span></span></div>
</section>

<h2 class="section-title abs" style="top:770px;font-size:26px">Your One-Stop <span class="red">Shop For</span> Custom Team Gear</h2>

<div class="gear abs">
  <article class="gear-card">
    <div class="pic" role="img" aria-label="Green and black football uniforms" style="background:linear-gradient(180deg,#eef3ec,#c9dcc4)"></div>
    <div class="info"><h3>Custom Uniforms</h3><p>Fully personalized for your team with colors, logos, and player names.</p></div>
  </article>
  <article class="gear-card">
    <div class="pic" role="img" aria-label="White printed t-shirt" style="background:linear-gradient(180deg,#f0f1f4,#d3d7de)"></div>
    <div class="info"><h3>Custom Shirt Creator</h3><p>Upload your design and see it instantly on your garment.</p></div>
  </article>
  <article class="gear-card">
    <div class="pic" role="img" aria-label="Row of white delivery vans" style="background:linear-gradient(180deg,#a9b2ba,#6a7179)"></div>
    <div class="info"><h3>Quality &amp; Comfort</h3><p>Premium materials built to perform on and off the field.</p></div>
  </article>
  <article class="gear-card">
    <div class="pic" role="img" aria-label="Courier handing over a parcel" style="background:linear-gradient(180deg,#dfe3e7,#b3bbc3)"></div>
    <div class="info"><h3>Fast &amp; Reliable Delivery</h3><p>Get your gear on time for every game or event.</p></div>
  </article>
</div>

<div class="locker-photo abs" role="img" aria-label="Locker room with yellow jerseys hanging in lockers"></div>
<div class="locker-copy abs">
  <h2 class="split-title">Step Into The <span class="red">Locker Room</span></h2>
  <p>Discover our wide selection of team uniforms and sports gear for champions. From gloves and shoes to practice equipment, we have everything your team needs: high quality, comfortable, and ready for game day for basketball, football and baseball.</p>
  <p>Explore our wide range of team uniforms and accessories designed for champions. From gloves and shoes to practice gear, we have everything your team needs to look and perform their best.</p>
  <span class="btn btn-red" style="margin-top:20px">Shop Locker Room</span>
</div>

<section class="uniforms abs">
  <svg width="1200" height="420" viewBox="0 0 1200 420" aria-hidden="true">
    <polygon points="620,0 1200,0 1200,420 820,420" fill="#2666b8"/>
    <polygon points="760,0 1200,0 1200,300" fill="#2b6dc0"/>
  </svg>
  <div class="uniforms-copy abs">
    <h2>Custom <span class="red">Uniforms</span> For Every Team</h2>
    <p>Build your team's identity with fully customizable uniforms. Pick colors, add logos, numbers, and names to create a look your players will love.</p>
    <span class="btn btn-red">Design Your Uniform</span>
  </div>
  <div class="jersey abs" role="img" aria-label="Black and yellow team jersey"></div>
</section>

<div class="shirt-photo abs" role="img" aria-label="Laptop showing a shirt design tool"></div>
<div class="shirt-copy abs">
  <h2 class="split-title">Create Your <span class="red">Perfect Shirt</span></h2>
  <p>Our easy-to-use shirt creator lets you upload your own graphics, logos, or text. Preview your design in real time and order with confidence.<br>Upload your custom shirt in just a few simple steps.<br>Upload your own graphics, logos, or text with ease.<br>See your design instantly with live previews.<br>Choose from multiple colors, sizes, and styles.<br>Perfect for teams, events, and everyday wear.<br>High quality printing that lasts game after game.</p>
  <span class="btn btn-blue">Start Designing Now</span>
</div>

<h2 class="section-title abs" style="top:2852px;font-size:26px">Top Brands For Top <span class="red">Performance</span></h2>
<p class="brands-sub abs">We partner with trusted sports brands to ensure quality, durability, and style.</p>
<div class="brand-row abs">
  <div class="brand-chip"><span class="dot"></span>Kordyn</div>
  <div class="brand-chip"><span class="dot"></span>Maxo</div>
  <div class="brand-chip"><span class="dot"></span>Tallet</div>
  <div class="brand-chip"><span class="dot"></span>Vorra</div>
  <div class="brand-chip"><span class="dot"></span>Pexi</div>
</div>

<section class="about abs">
  <h2>Who We Are</h2>
  <p>We are passionate about helping teams show up and win on the field. With years of experience in custom sports apparel, we deliver high quality uniforms, strong service, and gear that supports your team's best.</p>
  <span class="btn btn-blue">Learn More About Us</span>
</section>

<footer class="site-footer abs">
  <div class="brand footer-brand abs"><span class="mark"></span>Rivet Athletic Supply</div>
  <nav class="footer-links abs">
    <span>Home</span><span>Locker Room</span><span>Custom Uniforms</span><span>Custom Shirt Creator</span><span>Brands</span><span>About Us</span>
  </nav>
  <div class="socials abs"><span></span><span></span><span></span><span></span><span></span></div>
  <div class="footer-rule abs"></div>
  <p class="copyright abs">© 2025 Rivet Athletic Supply. All rights reserved.</p>
</footer>
<div class="to-top abs"><svg width="34" height="34" viewBox="0 0 34 34" aria-hidden="true"><path d="M11 19 L17 13 L23 19" stroke="#fff" stroke-width="2" fill="none"/></svg></div>

</body>
</html>
```